Our company TrulaPay, an online processor of payments is seeking talented submissions for our website redesign. The winning design will be chopped up and converted into a WordPress theme to allow for easy content additions and updates.

We are looking for modern designs that rival current websites in our industry (plimo.example, zanquetto.example, holvix.example, brandle.example, quillmarkcharges.example, evensplitcharges.example, KoboRun.example).

Our company is seeking to expand our reach to software developers and engineers who are either integrating our payment platform into their offerings or are engineering a custom solution for the company they work for and are in need of a payment platform such as our own.

We currently work with hundreds of different business partners whom either resell our services or integrate our processing capabilities into their software (which they sell). We also must communicate effectively to end users, businesses, who seek us out directly for their payment processing needs.

We are open to different color schemes but would ultimately like them to be somewhat inline with our current logo (see attached). Our website needs to instill security and confidence to any current and/or potential user as we are trusted with private and sensitive information.

We are seeking submissions from qualified; individual freelancers, freelance teams, and agencies who can attack this project in its entirety. Since this project is a total redesign, we would like submissions that have the capability to design any custom graphics, icons, buttons, and illustrations in line with our industry, capabilities, offerings, and content. We are looking for someone to design our new website and would prefer a vendor who can also help us to design elements (graphics, illustrations, charts, workflows) within our website.

Designs will be converted into a wordpress theme and we would like to utilize widgets for as many areas as possible to make editing and updating easy.

We are seeking the creation of a few unique pages but many of the pages for the majority of our content will just be internal content pages which will be duplicated.

We will likely contract with the winning submission for future work.

Please see Design Reference Document for more information

Target Market(s)

Resellers
Merchant Service Providers
Software Developers
Independent Sales Organizations (ISOs)
App Builders
Mobile App Builders
Independent Software Developers
Organizational Software Developers
Businesses who need to accept payments
Governments
Municipalities
Schools
DMVs
Courts
Retailers
Medical Offices
Hosipitals
Clinics
Dr. Offices
Gyms
Churches
Non-Profits
Software Companies
Technology Companies
Startups

• Logo cannot change drastically.

```html
<!DOCTYPE html>
<html lang="en">
<head>
<meta charset="utf-8">
<title>TrulaPay – Payment Processing</title>
<link rel="stylesheet" href="https://fonts.googleapis.com/css2?family=Open+Sans:ital,wght@0,300;0,400;0,600;0,700;1,400&family=Ubuntu:wght@400;500&display=swap">
<style>
:root{
  --brand:#2a3d8f;
  --blue:#2d5fad;
  --navy:#332f66;
  --hero:#5c56b4;
  --strip:#4a40ad;
  --pale:#f1f4f6;
  --lilac:#e4e1f5;
  --red:#e54a63;
  --teal:#17a69b;
  --ink:#333;
  --muted:#666;
  --white:#fff;
}
*{margin:0;padding:0;box-sizing:border-box}
html,body{width:806px;height:1200px;overflow:hidden;background:var(--white)}
body{position:relative;font-family:"Open Sans",Arial,sans-serif;color:var(--ink)}
.abs{position:absolute}
.wordmark{font-family:"Open Sans",Arial,sans-serif;font-weight:700;font-size:14px;color:var(--brand);letter-spacing:-.2px}

/* header */
.site-header{left:0;top:0;width:806px;height:34px;background:var(--white);border-bottom:1px solid #ddd}
.top-links{top:15px;left:426px;font-size:6px;display:flex;gap:8px;color:#222}
.login{top:15px;left:548px;font-size:6px;font-weight:600;color:var(--brand)}
.social{top:11px;width:14px;height:14px}
.main-nav{left:0;top:34px;width:806px;height:29px;background:#f4f4f4;border-bottom:1px solid #e3e3e3}
.main-nav span{position:absolute;top:11px;font-size:6.5px;font-weight:600;color:#555}
.main-nav .active{color:var(--brand)}

/* hero */
.hero{left:0;top:63px;width:806px;height:226px;background:linear-gradient(120deg,#6560bb,#5650ad 60%,#4d48a4)}
.hero h1{position:absolute;top:28px;width:806px;text-align:center;font-weight:300;font-size:18px;color:var(--white)}
.hero-icon{position:absolute;top:74px;width:58px;height:58px;border-radius:4px}
.btn{position:absolute;display:flex;align-items:center;justify-content:center;font-size:8px;color:var(--white);border-radius:2px}
.trust-strip{left:0;top:289px;width:806px;height:44px;background:var(--strip)}
.badge{position:absolute;background:rgba(255,255,255,.75);border-radius:2px}
.divider{position:absolute;top:8px;width:1px;height:28px;background:rgba(255,255,255,.35)}

/* features */
.features{left:0;top:333px;width:806px;height:139px;background:var(--pale)}
.feature{position:absolute;top:0;width:124px;text-align:center}
.feature-icon{margin:16px auto 0;width:52px;height:46px}
.feature h3{margin-top:14px;font-weight:400;font-size:11px;color:#222}
.feature p{margin:9px auto 0;padding:3px 6px;font-size:6px;line-height:10px;color:var(--muted)}
.feature.highlight h3{color:var(--blue)}
.feature.highlight p{background:#2a4fa8;color:var(--white);height:37px}

/* intro */
.intro-title{top:494px;width:806px;text-align:center;font-family:"Ubuntu",sans-serif;font-size:18px;color:var(--blue)}
.intro-sub{top:520px;width:806px;text-align:center;font-style:italic;font-size:7px;color:var(--red)}
.intro-text{left:152px;width:494px;font-size:7.3px;line-height:10px;color:#333}

/* merchant */
.merchant{left:0;top:617px;width:806px;height:192px;background:var(--lilac)}
.merchant h2{position:absolute;left:359px;top:25px;font-family:"Ubuntu",sans-serif;font-weight:400;font-size:18px;color:var(--blue)}
.service{position:absolute;font-size:8px;color:#333;display:flex;align-items:center;gap:12px}
.service svg{width:7px;height:8px}

/* developers */
.dev-title{left:152px;top:823px;font-family:"Ubuntu",sans-serif;font-size:18px;color:var(--blue)}
.code-box{left:151px;top:866px;width:186px;height:114px;background:#e8e8ea;padding:13px 16px;font-size:7px;line-height:12px;color:#333;white-space:pre}
.lang{position:absolute;left:397px;font-size:8px;display:flex;align-items:center;gap:12px;color:#333}
.lang svg{width:14px;height:8px}

/* footer */
.footer{left:0;top:1041px;width:806px;height:115px;background:var(--navy);color:var(--white)}
.footer .wordmark{color:var(--white);font-size:11px;font-weight:400}
.f-col{position:absolute;top:11px}
.f-col h4{font-weight:400;font-size:10px;margin-bottom:10px}
.f-col a{display:block;font-size:6.5px;line-height:12px;color:#e6e6f3;text-decoration:none}
.newsletter{position:absolute;left:511px;top:11px;width:131px;text-align:center}
.newsletter h4{font-size:8px;font-weight:700;letter-spacing:.2px}
.input{margin-top:9px;height:24px;border:1px solid #5b8fa8;background:#3e3d73;font-size:7px;line-height:22px}
.subscribe{margin:15px auto 0;width:88px;height:24px;background:var(--teal);font-size:8px;font-weight:700;line-height:24px}
.legal{left:0;top:1156px;width:806px;height:44px;background:#ececec;padding:15px 0 0 154px;font-size:6.3px;line-height:8px;color:#333}
</style>
</head>
<body>

<header class="abs site-header">
  <div class="abs wordmark" style="left:152px;top:9px">TrulaPay</div>
  <nav class="abs top-links"><span>API Guide</span><span>FAQ</span><span>About Us</span><span>Contact</span></nav>
  <div class="abs login">LOGIN | SIGNUP</div>
  <span class="abs social" style="left:604px;background:#3b5a9a" aria-label="Friendwall"></span>
  <span class="abs social" style="left:620px;background:#2fa9e0" aria-label="Chirply"></span>
  <span class="abs social" style="left:636px;background:#d9473b" aria-label="Circlet"></span>
</header>

<nav class="abs main-nav">
  <span class="active" style="left:323px">HOME</span>
  <span style="left:361px">SOLUTIONS</span>
  <span style="left:417px">PARTNERS</span>
  <span style="left:468px">RESOURCES</span>
  <span style="left:524px">DEVELOPERS</span>
  <span style="left:583px">COMPANY</span>
  <span style="left:634px">BLOG</span>
</nav>

<section class="abs hero" role="img" aria-label="Blurred office desk photograph tinted purple">
  <h1>Making payment processing fast, easy and flexible.</h1>
  <div class="hero-icon" style="left:258px;background:var(--red)" role="img" aria-label="Office building icon"></div>
  <div class="hero-icon" style="left:490px;background:var(--teal)" role="img" aria-label="Code document icon"></div>
  <div class="btn" style="left:229px;top:163px;width:123px;height:24px;background:var(--red)">BUSINESSES CLICK HERE</div>
  <div class="btn" style="left:454px;top:163px;width:123px;height:24px;background:var(--teal)">DEVELOPERS CLICK HERE</div>
</section>

<section class="abs trust-strip" aria-label="Memberships and accepted cards">
  <span class="badge" style="left:153px;top:16px;width:33px;height:12px"></span>
  <span class="badge" style="left:223px;top:16px;width:59px;height:12px"></span>
  <span class="divider" style="left:325px"></span>
  <span class="badge" style="left:352px;top:16px;width:18px;height:11px"></span>
  <span class="badge" style="left:381px;top:16px;width:18px;height:11px"></span>
  <span class="badge" style="left:410px;top:16px;width:18px;height:11px"></span>
  <span class="badge" style="left:440px;top:16px;width:18px;height:11px"></span>
  <span class="divider" style="left:485px"></span>
  <span class="badge" style="left:534px;top:14px;width:46px;height:16px"></span>
  <span class="badge" style="left:585px;top:14px;width:16px;height:16px"></span>
</section>

<section class="abs features">
  <div class="feature" style="left:142px">
    <svg class="feature-icon" viewBox="0 0 52 46"><rect x="3" y="6" width="40" height="28" rx="3" fill="#2a4fa8"/><rect x="3" y="14" width="40" height="5" fill="#fff"/><rect x="8" y="24" width="16" height="3" fill="#7fa0e0"/><rect x="30" y="24" width="18" height="14" rx="2" fill="#ddd"/></svg>
    <h3>Payment Solutions</h3>
    <p>Lorem ipsum dolor sit amet, con-sectetuer adipiscing elit, sed diam nonummy nibh</p>
  </div>
  <div class="feature highlight" style="left:276px">
    <svg class="feature-icon" viewBox="0 0 52 46"><rect x="6" y="4" width="34" height="30" rx="2" fill="none" stroke="#ccc" stroke-width="2"/><line x1="6" y1="10" x2="40" y2="10" stroke="#ccc" stroke-width="2"/><rect x="28" y="18" width="16" height="22" fill="#fff" stroke="#bbb" stroke-width="1.5"/><line x1="31" y1="25" x2="41" y2="25" stroke="#bbb"/><line x1="31" y1="29" x2="41" y2="29" stroke="#bbb"/><line x1="31" y1="33" x2="41" y2="33" stroke="#bbb"/></svg>
    <h3>Standard Api Guide</h3>
    <p>Lorem ipsum dolor sit amet, con-sectetuer adipiscing elit, sed diam nonummy nibh</p>
  </div>
  <div class="feature" style="left:408px">
    <svg class="feature-icon" viewBox="0 0 52 46"><rect x="4" y="8" width="34" height="26" rx="4" fill="#2a4fa8"/><rect x="26" y="16" width="14" height="10" rx="2" fill="#6f93d8"/><rect x="32" y="20" width="18" height="18" rx="2" fill="none" stroke="#ccc" stroke-width="1.5"/></svg>
    <h3>Reliable Payments</h3>
    <p>Lorem ipsum dolor sit amet, con-sectetuer adipiscing elit, sed diam nonummy nibh</p>
  </div>
  <div class="feature" style="left:530px">
    <svg class="feature-icon" viewBox="0 0 52 46"><path d="M16 18 v-6 a8 8 0 0 1 16 0 v6" fill="none" stroke="#2a4fa8" stroke-width="4"/><rect x="12" y="18" width="24" height="20" rx="2" fill="#2a4fa8"/><circle cx="24" cy="26" r="3" fill="#fff"/><rect x="23" y="27" width="2" height="6" fill="#fff"/><rect x="34" y="28" width="12" height="12" rx="2" fill="#ccc"/></svg>
    <h3>Anti Fraud Measures</h3>
    <p>Lorem ipsum dolor sit amet, con-sectetuer adipiscing elit, sed diam nonummy nibh</p>
  </div>
</section>

<h2 class="abs intro-title" style="font-weight:400">Payment Processing for the 21st Century.</h2>
<p class="abs intro-sub">TrulaPay provides the software, technology, and platform for multi-channel payment acceptance.</p>
<p class="abs intro-text" style="top:552px">Since 1992 we have been helping merchants streamline their payment acceptance. Whether your acceptance needs are online, at the poin-of-sale, or mobile; TrulaPay can help.</p>
<p class="abs intro-text" style="top:581px">We provide both “out-of -the-box ” and custom solutions for your company or organization to begin t aking paymentsin line with your needs and desires.</p>

<section class="abs merchant">
  <svg class="abs" style="left:485px;top:0" width="18" height="9" viewBox="0 0 18 9"><polygon points="0,0 18,0 9,9" fill="#fff"/></svg>
  <div class="abs" style="left:153px;top:36px;width:129px;height:129px;border-radius:50%;background:var(--red)" role="img" aria-label="Illustration of a merchant holding a dollar coin"></div>
  <h2>Merchant Payment Services</h2>
  <div class="service" style="left:359px;top:77px"><svg viewBox="0 0 7 8"><polygon points="0,0 7,4 0,8" fill="var(--red)"/></svg>Recuring Billing</div>
  <div class="service" style="left:359px;top:101px"><svg viewBox="0 0 7 8"><polygon points="0,0 7,4 0,8" fill="var(--red)"/></svg>Virtual Terminal</div>
  <div class="service" style="left:359px;top:125px"><svg viewBox="0 0 7 8"><polygon points="0,0 7,4 0,8" fill="var(--red)"/></svg>Scan Checks</div>
  <div class="service" style="left:359px;top:149px"><svg viewBox="0 0 7 8"><polygon points="0,0 7,4 0,8" fill="var(--red)"/></svg>Tallybook Integration</div>
  <div class="service" style="left:523px;top:77px"><svg viewBox="0 0 7 8"><polygon points="0,0 7,4 0,8" fill="var(--red)"/></svg>Website Payment Form</div>
  <div class="service" style="left:523px;top:101px"><svg viewBox="0 0 7 8"><polygon points="0,0 7,4 0,8" fill="var(--red)"/></svg>Transaction API</div>
  <div class="service" style="left:523px;top:125px"><svg viewBox="0 0 7 8"><polygon points="0,0 7,4 0,8" fill="var(--red)"/></svg>Electronic Invoicing</div>
  <div class="service" style="left:523px;top:149px"><svg viewBox="0 0 7 8"><polygon points="0,0 7,4 0,8" fill="var(--red)"/></svg>Mobile</div>
</section>

<h2 class="abs dev-title" style="font-weight:400">Developer tools - TrulaPay API</h2>
<pre class="abs code-box">function create Transactions() {
$cc = array(
'ss2324',
'John Doe',
32.40
)
$trulapay-&gt;charge($tran);</pre>
<div class="lang" style="top:868px"><svg viewBox="0 0 14 8"><path d="M4 1 L1 4 L4 7 M10 1 L13 4 L10 7 M8 0 L6 8" fill="none" stroke="#4fb6e0" stroke-width="1.2"/></svg>Curl</div>
<div class="lang" style="top:888px"><svg viewBox="0 0 14 8"><path d="M4 1 L1 4 L4 7 M10 1 L13 4 L10 7 M8 0 L6 8" fill="none" stroke="#4fb6e0" stroke-width="1.2"/></svg>PHP</div>
<div class="lang" style="top:908px"><svg viewBox="0 0 14 8"><path d="M4 1 L1 4 L4 7 M10 1 L13 4 L10 7 M8 0 L6 8" fill="none" stroke="#4fb6e0" stroke-width="1.2"/></svg>.Net</div>
<div class="lang" style="top:928px"><svg viewBox="0 0 14 8"><path d="M4 1 L1 4 L4 7 M10 1 L13 4 L10 7 M8 0 L6 8" fill="none" stroke="#4fb6e0" stroke-width="1.2"/></svg>Python</div>
<div class="lang" style="top:948px"><svg viewBox="0 0 14 8"><path d="M4 1 L1 4 L4 7 M10 1 L13 4 L10 7 M8 0 L6 8" fill="none" stroke="#4fb6e0" stroke-width="1.2"/></svg>Java</div>
<div class="lang" style="top:968px"><svg viewBox="0 0 14 8"><path d="M4 1 L1 4 L4 7 M10 1 L13 4 L10 7 M8 0 L6 8" fill="none" stroke="#4fb6e0" stroke-width="1.2"/></svg>Ruby</div>
<div class="abs" style="left:519px;top:848px;width:129px;height:129px;border-radius:50%;background:var(--teal)" role="img" aria-label="Illustration of a monitor showing code"></div>
<div class="btn" style="left:152px;top:998px;width:88px;height:24px;background:var(--red)">SIGN UP</div>

<footer class="abs footer">
  <div class="abs wordmark" style="left:157px;top:11px">TrulaPay</div>
  <div class="f-col" style="left:159px;top:31px"><a>Home</a><a>Soulutions</a><a>Partners</a><a>resources</a><a>Developers</a></div>
  <div class="f-col" style="left:233px"><h4>Company</h4><a>About Us</a><a>Contact Us</a><a>Blog</a></div>
  <div class="f-col" style="left:300px"><h4>Help</h4><a>Help &amp; Support</a><a>API Guide</a><a>FAQ</a></div>
  <div class="f-col" style="left:370px"><h4>Info</h4><a>Login</a><a>Signup</a><a>Privacy Policy</a><a>Terms of Use</a></div>
  <div class="f-col" style="left:439px"><h4>Connect</h4><a>Friendwall</a><a>Chirply</a><a>Circlet</a></div>
  <div class="newsletter">
    <h4>JOIN THE NEWSLETTER</h4>
    <div class="input">yourname@mailbox.example</div>
    <div class="subscribe">SUBSCRIBE</div>
  </div>
</footer>

<div class="abs legal">©2013 TrulaPay® | ACH Payment Processing, All Rights Reserved.<br>TrulaPay® and the TrulaPay® logo are registered trademarks of TrulaPay, Inc.</div>

</body>
</html>
```